Tallis & Co Flyer (tri-fold) Accounting Firm

We are an accounting firm that provides loan broking services. We would like the brochure to look sophisticated but not too formal.

We would like to add some background colour to the flyer/brochure (attached in word and PDF version) in the following green (Hex Colour #94c947) in different styles/patterns etc.

Guidelines:

• We envisage that the green would cover approximately 30% of the background

• Do not change any of the content

• Change fonts as required

• The wording, titles/headings and background can be a combination of the green colour #94c947, black and white.

• We are happy to use multiple shadings of the green colour above to give contrast and depth

• We would like a 3-5mm bleed around the edges.

• Please remove black page break lines are to disappear (not sure how to remove on word document).

• Please stretch all images to the edge of the bleed (except for KRVA, Ledgerwise Planner, Homestead Lending and PlainNest 520 logos).

• Please insert different icons for phone, fax and email, e.g. an image of a telephone next to our number instead of the symbol “P”.

We have included a copy of a business card as an example of our existing style we wish to retain in the brochure.

Please provide appropriate file types to enable publishing of brochures.

Target Market(s)

Business owners and individuals requiring accounting and services, people requiring loans/refinance, superannuation retirees

Industry/Entity Type

Accounting

Font styles to use
Other font styles liked:
• Refer to business card font

Colors
abd037

Requirements
Must have
• Must use our Tallis & Co logo green with black text (as in the attached brochure).
Nice to have
• The design concept does not need to necessarily include the KRVA, Ledgerwise Planner, Homestead Lending and PlainNest 520 logos, this may create a simpler cleaner look. I'd like to look at the brochure design with and without those additional logos for comparison purposes.

```html
<!DOCTYPE html>
<html lang="en">
<head>
<meta charset="utf-8">
<title>Tallis &amp; Co – Tri-fold Brochure</title>
<link href="https://fonts.googleapis.com/css2?family=Open+Sans:ital,wght@0,400;0,600;0,700;1,600;1,700&display=swap" rel="stylesheet">
<style>
  :root{
    --green:#94c947;
    --green-deep:#6f9e2c;
    --slate:#4b4f5c;
    --ink:#1f2226;
    --white:#ffffff;
    --paper:#e8e8e6;
    --photo-warm:#b99378;
    --photo-cool:#9fb0bd;
  }
  *{box-sizing:border-box;margin:0;padding:0}
  html,body{width:901px;height:1200px;overflow:hidden;background:var(--paper)}
  body{font-family:"Open Sans",Arial,sans-serif;color:var(--ink)}
  .canvas{position:relative;width:901px;height:1200px;overflow:hidden}
  .sheet{position:absolute;left:30px;width:841px;height:555px;display:flex;box-shadow:0 3px 10px rgba(0,0,0,.25)}
  .sheet--outside{top:35px}
  .sheet--inside{top:610px}
  .panel{position:relative;width:280px;height:100%;overflow:hidden}
  .panel--green{background:var(--green)}
  .panel--slate{background:var(--slate);color:var(--white)}
  .panel + .panel{width:281px}
  .pad{padding:0 20px}
  p{font-size:8.6px;line-height:1.36;margin-bottom:6px}
  h2{font-size:13px;font-weight:700;margin-bottom:5px}
  h3{font-size:11px;font-weight:700;color:var(--green);margin:6px 0 4px}
  .brand{display:flex;align-items:center;gap:8px}
  .brand__mark{width:26px;height:26px;background:var(--ink)}
  .brand__name{font-size:17px;font-weight:600;letter-spacing:1px;color:var(--ink)}
  .map{position:absolute;left:20px;top:38px;width:240px;height:170px;background:linear-gradient(135deg,#f1efe9,#dcdad3)}
  .contact{position:absolute;left:20px;top:228px;right:20px}
  .contact h2{font-size:12px}
  .contact li{list-style:none;display:flex;align-items:center;gap:7px;font-size:8.6px;margin-bottom:5px}
  .contact svg{width:11px;height:11px;flex:none}
  .outside-brand{position:absolute;left:20px;bottom:52px}
  .origins{padding-top:16px}
  .origins__head{font-size:12px;font-weight:700;letter-spacing:.5px}
  .origins__sub{font-size:11px;font-weight:700;color:var(--green);margin-bottom:6px}
  .founder{float:left;width:54px;margin:0 8px 4px 0}
  .founder__portrait{width:54px;height:64px;background:linear-gradient(#d9d9d9,#8e9096)}
  .founder__name{font-size:7.5px;font-weight:700;color:var(--green);line-height:1.15;margin-top:3px}
  .founder__role{font-size:6px;line-height:1.2}
  .quote-by{font-size:8px;font-style:italic;font-weight:700;color:var(--green);margin-bottom:10px}
  .book{position:absolute;right:-14px;top:-14px;width:82px;height:82px;border-radius:50%;background:var(--slate);color:var(--white);text-align:center;font-size:9px;line-height:1.15;padding:24px 12px 0 6px}
  .book strong{color:var(--green)}
  .front-brand{position:absolute;left:20px;top:66px}
  .front-photo{position:absolute;left:0;top:124px;width:100%;height:172px;background:linear-gradient(135deg,#c9c2b8,#8b8a86 60%,#b7b1a6)}
  .ticks{position:absolute;left:22px;top:320px;list-style:none}
  .ticks li{display:flex;align-items:center;gap:6px;font-size:10px;margin-bottom:7px}
  .ticks--static{position:static}
  .ticks--small li{font-size:8.6px;margin-bottom:5px}
  .tick{width:11px;height:11px;flex:none}
  .badges{position:absolute;left:30px;right:30px;bottom:40px;display:flex;justify-content:space-between}
  .badge{width:54px;height:30px;background:var(--ink);opacity:.75;border-radius:3px}
  .inside-top{position:absolute;left:0;top:0;width:100%;height:385px}
  .inside-photo{position:absolute;left:0;bottom:0;width:100%;height:170px}
  .inside-photo--cafe{background:linear-gradient(135deg,#e4dcd2,var(--photo-warm) 55%,#7a4a3a)}
  .inside-photo--desk{background:linear-gradient(135deg,#e9ecef,var(--photo-cool) 60%,#5f6b77)}
  .inside-photo--garden{background:linear-gradient(135deg,#f0c27a,#c98a4b 55%,#7e8f45)}
  .tax{padding-top:16px}
  .tax h2{margin-bottom:3px}
  .business-head{margin-top:4px}
  .including{font-size:8.6px;font-weight:700;margin-bottom:4px}
  .two-col{display:grid;grid-template-columns:1fr 1fr;column-gap:4px}
  .partner-row{display:flex;gap:12px;margin-top:6px}
  .partner{display:flex;align-items:center;gap:4px;background:var(--white);padding:3px 6px;font-size:8px;font-weight:700;color:var(--ink)}
  .partner i{width:8px;height:8px;background:var(--green-deep);display:block}
  .partner--bare{padding:0}
  .mortgage-photo{height:150px;background:linear-gradient(160deg,#c9ced4,#7d8794 70%,#58606b)}
  .loan{padding-top:14px}
  .loan h2{font-size:11.5px}
  .loan .ticks{margin-top:4px}
  .loan .ticks li{color:var(--white)}
  .free{color:var(--green)}
  .loan-cta{font-size:9.5px;font-style:italic;font-weight:700;color:var(--green);text-align:center;margin-top:10px;line-height:1.3}
  .partner-box{position:absolute;left:50%;transform:translateX(-50%);bottom:8px;background:var(--white);padding:6px 10px}
  .super{padding-top:16px}
  .super-cta{font-size:9.5px;font-style:italic;font-weight:700;text-align:center;margin-top:10px;line-height:1.3}
</style>
</head>
<body>
<svg width="0" height="0" style="position:absolute">
  <symbol id="tick-dark" viewBox="0 0 12 12"><circle cx="6" cy="6" r="5.3" fill="none" stroke="#1f2226"/><path d="M3.4 6.2l1.8 1.8 3.5-3.8" stroke="#1f2226" stroke-width="1.3" fill="none"/></symbol>
  <symbol id="tick-light" viewBox="0 0 12 12"><circle cx="6" cy="6" r="5.3" fill="none" stroke="#ffffff"/><path d="M3.4 6.2l1.8 1.8 3.5-3.8" stroke="#ffffff" stroke-width="1.3" fill="none"/></symbol>
</svg>
<div class="canvas">

  <section class="sheet sheet--outside">
    <div class="panel panel--green">
      <div class="map" role="img" aria-label="Street map showing the office location"></div>
      <div class="contact">
        <h2>Contact Us</h2>
        <ul>
          <li><svg viewBox="0 0 12 12"><path d="M6 0a4 4 0 0 0-4 4c0 3 4 8 4 8s4-5 4-8a4 4 0 0 0-4-4zm0 5.5A1.5 1.5 0 1 1 6 2.5a1.5 1.5 0 0 1 0 3z" fill="#1f2226"/></svg><span>412 Harbour Road<br>Kingsford West SA 5092</span></li>
          <li><svg viewBox="0 0 12 12"><path d="M2.5 1l2 .5 1 2.5-1.3 1a6 6 0 0 0 2.8 2.8l1-1.3 2.5 1 .5 2c-.5.6-1.3.9-2 .8C5 9.8 2.2 7 1.7 3.5c-.1-.8.2-1.9.8-2.5z" fill="#1f2226"/></svg><span>(08) 8000 1234</span></li>
          <li><svg viewBox="0 0 12 12"><rect x="1" y="2.5" width="10" height="7" rx="1" fill="#1f2226"/><path d="M1.5 3l4.5 3.5L10.5 3" stroke="#94c947" stroke-width="1" fill="none"/></svg><span>admin@tallis-co.example</span></li>
          <li><svg viewBox="0 0 12 12"><circle cx="6" cy="6" r="5" fill="none" stroke="#1f2226" stroke-width="1.2"/><path d="M1 6h10M6 1c-2 2.5-2 7.5 0 10M6 1c2 2.5 2 7.5 0 10" stroke="#1f2226" stroke-width=".9" fill="none"/></svg><span>tallis-co.example</span></li>
        </ul>
      </div>
      <div class="brand outside-brand"><span class="brand__mark"></span><span class="brand__name">TALLIS &amp; CO</span></div>
    </div>

    <div class="panel panel--slate">
      <div class="pad origins">
        <div class="origins__head">TALLIS &amp; CO</div>
        <div class="origins__sub">Our Origins</div>
        <div class="founder">
          <div class="founder__portrait" role="img" aria-label="Portrait of the firm's founder"></div>
          <div class="founder__name">Edmund Tallis</div>
          <div class="founder__role">BBus, MTax, CTA<br>PRINCIPAL</div>
        </div>
        <p>The firm's origins were established in 1991 when Edmund Tallis commenced public practice in Seacliff Bay. In 2004, the firm relocated to Kingsford West as the client base grew.</p>
        <p>At Tallis &amp; Co, we understand that the world is constantly changing, however when it comes to values we believe some things should never change.</p>
        <p>Values such as trust, integrity and confidentiality are as fundamental to us in our business relationships as they are in our everyday lives.</p>
        <h3>Client Testimonials</h3>
        <p>We have been a client of Tallis 18 Marlow St North Kelby for over 15 years and are very happy with their services. Tallis &amp; Co has been the perfect business advice and support. Ed and his team place customer satisfaction at the top of their agenda and back it up with all of the knowledge you could ever need. Any enquiry or concern is swiftly dealt with and the support is second to none.</p>
        <p>Over the years Tallis &amp; Co have been an important and stable part of our company and we will enjoy using their services in the future.</p>
        <div class="quote-by">Peter, Builder, Eastvale</div>
        <p>Our newsagency was fortunate to be a client of Tallis &amp; Co for over 20 years. We received amazing support by Ed and his team during a particularly difficult personal time, the sale of our family business. When the sale was complete, considering all the time we were afforded, we were amazed at the very small amount we had to pay for their amazing support.</p>
        <div class="quote-by">Rosalind, Seacliff Bay</div>
      </div>
    </div>

    <div class="panel panel--green">
      <div class="book">Book<br>for a <strong>FREE</strong><br>appointment<br>today!</div>
      <div class="brand front-brand"><span class="brand__mark"></span><span class="brand__name">TALLIS &amp; CO</span></div>
      <div class="front-photo" role="img" aria-label="Business people reviewing charts on a desk with coffee and a tablet"></div>
      <ul class="ticks">
        <li><svg class="tick"><use href="#tick-dark"/></svg>Accounting and Taxation</li>
        <li><svg class="tick"><use href="#tick-dark"/></svg>Mortgage and Finance</li>
        <li><svg class="tick"><use href="#tick-dark"/></svg>Self Managed Super Funds</li>
      </ul>
      <div class="badges"><span class="badge"></span><span class="badge"></span></div>
    </div>
  </section>

  <section class="sheet sheet--inside">
    <div class="panel">
      <div class="inside-top panel--green">
        <div class="pad tax">
          <h2>Tax Services</h2>
          <p>We prepare tax returns ranging from the simplest individual return to the most complex business.</p>
          <ul class="ticks ticks--small ticks--static">
            <li><svg class="tick"><use href="#tick-dark"/></svg>Individuals, partnerships, companies, trusts and SMSFs</li>
          </ul>
          <div class="including">Including:</div>
          <ul class="ticks ticks--small ticks--static two-col">
            <li><svg class="tick"><use href="#tick-dark"/></svg>Rental properties</li>
            <li><svg class="tick"><use href="#tick-dark"/></svg>Deceased estates</li>
            <li><svg class="tick"><use href="#tick-dark"/></svg>Capital Gains Tax</li>
            <li><svg class="tick"><use href="#tick-dark"/></svg>Tax Planning</li>
            <li><svg class="tick"><use href="#tick-dark"/></svg>Share Portfolios</li>
            <li><svg class="tick"><use href="#tick-dark"/></svg>ATO communications</li>
            <li><svg class="tick"><use href="#tick-dark"/></svg>GST, BAS and IAS</li>
          </ul>
          <h2 class="business-head">Own your own business?</h2>
          <p>We understand running a business is hard work. Let us work with you to help improve your business performance.</p>
          <ul class="ticks ticks--small ticks--static">
            <li><svg class="tick"><use href="#tick-dark"/></svg>New business start up</li>
            <li><svg class="tick"><use href="#tick-dark"/></svg>Purchase and sale of business</li>
            <li><svg class="tick"><use href="#tick-dark"/></svg>Asset protection</li>
            <li><svg class="tick"><use href="#tick-dark"/></svg>Succession planning</li>
            <li><svg class="tick"><use href="#tick-dark"/></svg>Purchase and sale of property</li>
            <li><svg class="tick"><use href="#tick-dark"/></svg>Budgeting and benchmarking</li>
            <li><svg class="tick"><use href="#tick-dark"/></svg>Cloud, KRVA &amp; Ledgerwise Planner software</li>
          </ul>
          <div class="partner-row">
            <span class="partner"><i></i>KRVA</span>
            <span class="partner"><i></i>Ledgerwise Planner</span>
          </div>
        </div>
      </div>
      <div class="inside-photo inside-photo--cafe" role="img" aria-label="Two smiling cafe owners standing in their shop"></div>
    </div>

    <div class="panel">
      <div class="inside-top panel--slate">
        <div class="mortgage-photo" role="img" aria-label="Businessman touching a screen showing the words Mortgage and Interest"></div>
        <div class="pad loan">
          <h2>Have you reviewed your loan lately?</h2>
          <p>We provide our clients with a <strong class="free">FREE</strong> annual review of their existing commercial and residential loan portfolio and can assist our clients in obtaining new loans.</p>
          <ul class="ticks ticks--small ticks--static">
            <li><svg class="tick"><use href="#tick-light"/></svg>Free annual loan portfolio review</li>
            <li><svg class="tick"><use href="#tick-light"/></svg>Selection of 25 residential lenders</li>
            <li><svg class="tick"><use href="#tick-light"/></svg>Selection of 8 commercial lenders</li>
            <li><svg class="tick"><use href="#tick-light"/></svg>Secure competitive rates available in the market</li>
          </ul>
          <div class="loan-cta">Simply give us a call and we will<br>handle the rest.</div>
        </div>
        <div class="partner-box"><span class="partner partner--bare"><i></i>Homestead Lending</span></div>
      </div>
      <div class="inside-photo inside-photo--desk" role="img" aria-label="Laptop and tablet showing finance software on a desk"></div>
    </div>

    <div class="panel">
      <div class="inside-top panel--green">
        <div class="pad super">
          <h2>Take control of your Super</h2>
          <p>SMSFs are a fast growing vehicle for investment, accounting for approximately one third of all superannuation assets with more than 6,500 funds being setup per quarter.</p>
          <p>The SMSF structure enables members to have the flexibility to <strong>CONTROL</strong> their investment strategy to suit their personal circumstances.</p>
          <ul class="ticks ticks--small ticks--static">
            <li><svg class="tick"><use href="#tick-dark"/></svg>SMSF Establishment/Rollover</li>
            <li><svg class="tick"><use href="#tick-dark"/></svg>Compliance obligations</li>
            <li><svg class="tick"><use href="#tick-dark"/></svg>Consultancy and strategic advice</li>
            <li><svg class="tick"><use href="#tick-dark"/></svg>Retirement strategies</li>
            <li><svg class="tick"><use href="#tick-dark"/></svg>Estate planning</li>
          </ul>
          <div class="super-cta">Speak to one of our consultants<br>about our SMSF services.</div>
        </div>
        <div class="partner-box"><span class="partner partner--bare"><i></i>PlainNest 520</span></div>
      </div>
      <div class="inside-photo inside-photo--garden" role="img" aria-label="Retired woman on the phone in a sunny garden with flowers"></div>
    </div>
  </section>

</div>
</body>
</html>
```